Website ui design required!

I require a web page ui design.
Theme: Outsourcing platform for developers and clients.
This website will be specifically for app/android/game/windows developers.
Anything that can be outsourced for app categories.
*App solutions
*Graphic design
*Marketing
*Project management
*mobile
*sdk intergration
*Developers
Basically if you want an app built on any platform, this website allows clients to connect with developers and other services surrounding that environment.
Please look at www.briskwork.com.au
Www.plorvin.com
Www.tefa.com
www.vormix.com
www.pellowind.com
Please make it look sleek and appealing.
I want this website to be the no.1 place for clients to source the best app developers worldwide. (random) I noticed these websites are 2 toned in color split, top and bottom.
All the best!!:)
Please take a look at the websites I mentioned.
Target Market(s)
Target market will be for anyone who wishes to
Find a developer, graphic artist, mobile apps, sdk integration,
app design, app consultation, web/mobile project management etc.
This is going to be an outsourcing platform for developers worldwide, also a place
For clients to hire manage and pay developers.
Industry/Entity Type
Graphic Design
Look and feel
Each slider illustrates characteristics of the customer's brand and the style your logo design should communicate.

```html
<!DOCTYPE html>
<html lang="en">
<head>
<meta charset="utf-8">
<title>Codara — outsourcing platform for developers and clients</title>
<link rel="stylesheet" href="https://fonts.googleapis.com/css2?family=Jura:wght@300;400;500;700&display=swap">
<style>
  :root {
    --backdrop: #b0b0b0;
    --sky: #45c0e8;
    --sun: #ffc600;
    --white: #ffffff;
    --paper: #ffffff;
    --footer-bg: #f4f4f4;
    --ink-soft: #9a9a9a;
    --ink-muted: #a8a8a8;
    --device-tone: #5ccaee;
  }
  * { box-sizing: border-box; margin: 0; padding: 0; }
  html, body {
    width: 1023px; height: 1200px; overflow: hidden;
    background: var(--backdrop);
    font-family: "Jura", sans-serif;
  }
  .page {
    position: absolute; left: 81px; top: 0;
    width: 853px; height: 1200px;
    background: var(--paper);
  }
  .hero {
    position: absolute; left: 0; top: 0; width: 853px; height: 459px;
    background: var(--sky);
  }
  .hero-pointer { position: absolute; left: 248px; top: 458px; }
  .brand {
    position: absolute; left: 143px; top: 26px;
    font-weight: 700; font-size: 62px; line-height: 1;
    color: var(--sun); letter-spacing: -1px;
  }
  .tagline {
    position: absolute; left: 143px; top: 102px;
    font-size: 14px; color: var(--white); font-weight: 500;
  }
  .search {
    position: absolute; left: 148px; top: 144px;
    width: 269px; height: 35px; background: var(--white);
    display: flex; align-items: center;
  }
  .search::before {
    content: ""; position: absolute; left: -5px; top: 12px;
    border-right: 5px solid var(--white);
    border-top: 5px solid transparent; border-bottom: 5px solid transparent;
  }
  .search-label { padding-left: 18px; font-size: 14px; color: var(--sky); font-weight: 500; }
  .search-icon { position: absolute; right: 0; top: 0; }
  .skills {
    position: absolute; left: 166px; top: 202px; list-style: none;
  }
  .skills li { font-size: 12.5px; line-height: 20.5px; color: var(--white); }
  .actions { position: absolute; left: 579px; top: 37px; }
  .action {
    display: block; width: 129px; height: 27px; margin-bottom: 12.5px;
    border: 2px solid var(--sun); color: var(--white);
    text-align: center; font-size: 15px; font-weight: 700; line-height: 23px;
    text-decoration: none;
  }
  .social { position: absolute; left: 738px; top: 13px; display: flex; gap: 2px; }
  .social span {
    width: 24px; height: 24px; border-radius: 50%; background: var(--white); display: block;
  }
  .devices {
    position: absolute; left: 143px; top: 264px; width: 565px; height: 158px;
    background: linear-gradient(180deg, rgba(255,255,255,0.05), rgba(255,255,255,0.18));
    border-radius: 4px;
  }
  .steps { position: absolute; left: 0; top: 530px; width: 853px; }
  .step { position: absolute; width: 188px; text-align: center; }
  .step-1 { left: 42px; }
  .step-2 { left: 332px; }
  .step-3 { left: 622px; }
  .step-badge { display: block; margin: 0 auto; }
  .step-title {
    margin-top: 10px; font-size: 31px; font-weight: 400; color: var(--sky); line-height: 1;
  }
  .step-text {
    margin-top: 38px; font-size: 9.5px; line-height: 12.4px;
    color: var(--ink-soft); text-align: justify;
  }
  .footer {
    position: absolute; left: 0; top: 876px; width: 853px; height: 324px;
    background: var(--footer-bg);
  }
  .footer-pointer { position: absolute; left: 538px; top: 0; }
  .footer-col { position: absolute; top: 74px; list-style: none; }
  .col-1 { left: 41px; top: 75px; }
  .col-2 { left: 331px; }
  .col-3 { left: 621px; top: 73px; }
  .footer-heading {
    font-size: 12.5px; color: var(--ink-soft); text-transform: uppercase;
    line-height: 20.5px; font-weight: 500;
  }
  .footer-col li { font-size: 12.5px; line-height: 20.5px; color: var(--ink-muted); }
  .footer-group + .footer-group { margin-top: 20px; }
  .copyright {
    position: absolute; left: 0; width: 853px; top: 292px;
    text-align: center; font-size: 9.5px; color: var(--ink-soft);
  }
</style>
</head>
<body>
<div class="page">
  <header class="hero">
    <div class="brand">Codara</div>
    <p class="tagline">outsourcing platform for developers and clients</p>

    <div class="search">
      <span class="search-label">Search for a skill</span>
      <svg class="search-icon" width="44" height="35" viewBox="0 0 44 35">
        <rect width="44" height="35" fill="#ffffff"/>
        <circle cx="19" cy="15" r="12" fill="none" stroke="#45c0e8" stroke-width="4"/>
        <line x1="28" y1="24" x2="36" y2="33" stroke="#45c0e8" stroke-width="5" stroke-linecap="round"/>
      </svg>
    </div>

    <ul class="skills">
      <li>App development</li>
      <li>Graphic design</li>
      <li>Marketing</li>
      <li>Project management</li>
    </ul>

    <nav class="actions">
      <a class="action" href="#">Register!</a>
      <a class="action" href="#">Login</a>
      <a class="action" href="#">Post a job!</a>
    </nav>

    <div class="social" aria-label="Social links">
      <span></span><span></span><span></span><span></span>
    </div>

    <div class="devices" role="img" aria-label="Line illustration of a phone, tablet, laptop and desktop monitor"></div>
  </header>

  <svg class="hero-pointer" width="67" height="58" viewBox="0 0 67 58">
    <polygon points="0,0 67,0 33.5,57" fill="#45c0e8"/>
  </svg>

  <section class="steps">
    <div class="step step-1">
      <svg class="step-badge" width="88" height="88" viewBox="0 0 88 88">
        <circle cx="44" cy="44" r="43" fill="#45c0e8"/>
        <circle cx="44" cy="44" r="37" fill="#ffc600"/>
        <rect x="31" y="33" width="26" height="3" fill="#fff"/>
        <rect x="31" y="42.5" width="26" height="3" fill="#fff"/>
        <rect x="31" y="52" width="26" height="3" fill="#fff"/>
      </svg>
      <h2 class="step-title">Hire</h2>
      <p class="step-text">Lorem ipsum dolor sit amet, consectetur adipisicing elit, sed do eiusmod tempor incididunt ut labore et dolore magna aliqua. Ut enim ad minim veniam, quis nostrud exercitation ullamco laboris nisi ut aliquip ex ea commodo consequat. Duis aute irure dolor in reprehenderit in voluptate velit esse cillum dolore eu fugiat nulla pariatur. Excepteur sint occaecat cupidatat non proident, sunt in culpa qui officia deserunt mollit anim id est laborum.</p>
    </div>
    <div class="step step-2">
      <svg class="step-badge" width="88" height="88" viewBox="0 0 88 88">
        <circle cx="44" cy="44" r="43" fill="#45c0e8"/>
        <circle cx="44" cy="44" r="37" fill="#ffc600"/>
        <g fill="#fff" transform="translate(44 44)">
          <rect x="-2.5" y="-14" width="5" height="28"/>
          <rect x="-2.5" y="-14" width="5" height="28" transform="rotate(45)"/>
          <rect x="-2.5" y="-14" width="5" height="28" transform="rotate(90)"/>
          <rect x="-2.5" y="-14" width="5" height="28" transform="rotate(135)"/>
          <circle r="10"/>
        </g>
        <circle cx="44" cy="44" r="4" fill="#ffc600"/>
      </svg>
      <h2 class="step-title">Manage</h2>
      <p class="step-text">Lorem ipsum dolor sit amet, consectetur adipisicing elit, sed do eiusmod tempor incididunt ut labore et dolore magna aliqua. Ut enim ad minim veniam, quis nostrud exercitation ullamco laboris nisi ut aliquip ex ea commodo consequat. Duis aute irure dolor in reprehenderit in voluptate velit esse cillum dolore eu fugiat nulla pariatur. Excepteur sint occaecat cupidatat non proident, sunt in culpa qui officia deserunt mollit anim id est laborum.</p>
    </div>
    <div class="step step-3">
      <svg class="step-badge" width="88" height="88" viewBox="0 0 88 88">
        <circle cx="44" cy="44" r="43" fill="#45c0e8"/>
        <circle cx="44" cy="44" r="37" fill="#ffc600"/>
        <text x="44" y="56" text-anchor="middle" font-family="Jura, sans-serif" font-weight="700" font-size="34" fill="#fff">$</text>
      </svg>
      <h2 class="step-title">Pay</h2>
      <p class="step-text">Lorem ipsum dolor sit amet, consectetur adipisicing elit, sed do eiusmod tempor incididunt ut labore et dolore magna aliqua. Ut enim ad minim veniam, quis nostrud exercitation ullamco laboris nisi ut aliquip ex ea commodo consequat. Duis aute irure dolor in reprehenderit in voluptate velit esse cillum dolore eu fugiat nulla pariatur. Excepteur sint occaecat cupidatat non proident, sunt in culpa qui officia deserunt mollit anim id est laborum.</p>
    </div>
  </section>

  <footer class="footer">
    <svg class="footer-pointer" width="67" height="57" viewBox="0 0 67 57">
      <polygon points="0,0 67,0 33.5,56" fill="#ffffff"/>
    </svg>

    <ul class="footer-col col-1">
      <li class="footer-heading">Company Info</li>
      <li>About Us</li>
      <li>Press</li>
      <li>Our Blog</li>
      <li>Careers</li>
      <li>Economy</li>
      <li>Terms of Service</li>
      <li>Privacy Policy</li>
      <li>Contact &amp; Support</li>
      <li>Resources</li>
    </ul>

    <ul class="footer-col col-2">
      <li class="footer-heading">Additional Services</li>
      <li>Enterprise Solutions</li>
      <li>Our Payroll</li>
      <li>Health Benefits</li>
    </ul>

    <div class="footer-col col-3">
      <ul class="footer-group" style="list-style:none">
        <li class="footer-heading">Connect With Us</li>
        <li>Affiliate Program</li>
        <li>Our Groups</li>
        <li>Partners</li>
      </ul>
      <ul class="footer-group" style="list-style:none">
        <li class="footer-heading">Our Clients</li>
        <li>Testimonials</li>
        <li>Feedback</li>
        <li>Experience</li>
      </ul>
    </div>

    <p class="copyright">© 2013 All Rights Reserved</p>
  </footer>
</div>
</body>
</html>
```